Redesign of Pledgebloom.com

We need a redesign of some key-pages on our crowdfunding website for mobile apps, PledgeBloom.com.

- Redesign of homepage
http://www.pledgebloom.com/en

- Redesign of project submission page
http://www.pledgebloom.com/en/submit-your-app/submit-your-app

- Redesign of browsing section
http://www.pledgebloom.com/en/fund-apps

- Redesign of project funding page
http://www.pledgebloom.com/en/fund-apps/sponsor/sketch-riddler?amount=5.00

Design should be highly focused on a great user experience for users of the platform, being in principal mobile developers. So we need a great user experience for mobile developers using our service.

Benchmark designs we particularly like are:
http://www.brimwagon.com/
http://www.tradeyourtool.com/landing/
http://www.vovari.com/

Design should have a more 'fun, happy to get involved' factor as it has nox.
Updates

Target Market(s)

mobile app developers

Industry/Entity Type

Crowdfunding

Requirements
Must have
• Submission forms must have explanation fields next to the form

Homepage should have design in whihc a introductary video can be integrated

```html
<!DOCTYPE html>
<html lang="en">
<head>
<meta charset="utf-8">
<title>PledgeBloom – Support new mobile apps</title>
<link rel="stylesheet" href="https://fonts.googleapis.com/css2?family=Open+Sans:wght@400;600;700;800&family=Arimo:wght@400;700&display=swap">
<style>
:root{
  --page:#e9ebec;
  --navy:#0b4a6b;
  --navy-dark:#073650;
  --panel-light:#5aa0dc;
  --green:#49b52a;
  --lime:#8ed32c;
  --magenta:#a5307d;
  --magenta-light:#b9529a;
  --ink:#2a2a2a;
  --muted:#8a8f93;
  --white:#ffffff;
}
*{box-sizing:border-box;margin:0;padding:0}
html,body{width:1200px;height:800px;overflow:hidden}
body{background:var(--page);font-family:"Open Sans",sans-serif;color:var(--ink);position:relative}
.abs{position:absolute}

.site-header{left:0;top:0;width:1200px;height:116px;background:linear-gradient(#e6e9eb,#d9dde0)}
.brand{left:100px;top:20px;display:flex;align-items:center;gap:10px;z-index:2}
.brand-mark{width:40px;height:40px;background:var(--navy);border-radius:6px}
.brand-name{font-size:26px;font-weight:700;color:var(--navy);letter-spacing:-.5px}
.hero-art{left:318px;top:0;width:440px;height:114px;background:linear-gradient(100deg,#f0c89a 0%,#e35a3a 25%,#3a8ad8 55%,#7ac43b 80%,#e8ebee 100%);opacity:.85;border-radius:0 0 40px 0}
.utility{left:745px;top:0;width:328px;height:28px;background:linear-gradient(#0f5c82,#07405e);border-radius:0 0 8px 8px;display:flex;justify-content:center;align-items:center;gap:8px;font-family:"Arimo",sans-serif;font-size:13px;color:var(--white)}
.utility span.sep{opacity:.8}
.lang{left:840px;top:28px;width:150px;height:22px;background:var(--white);border-radius:0 0 8px 8px;font-size:11px;font-weight:700;color:var(--navy);text-align:center;line-height:22px;box-shadow:0 1px 2px rgba(0,0,0,.2)}
.social{left:963px;top:93px;display:flex;gap:4px}
.social i{width:18px;height:18px;background:#3d6f9a;border-radius:3px;display:block}

.main-nav{left:0;top:116px;width:1200px;height:35px;background:linear-gradient(#147597,#0a4c6c 60%,#083f5b);border-top:1px solid #3c95b5}
.main-nav ul{list-style:none;position:absolute;left:140px;top:0;display:flex;gap:23px;line-height:35px;font-size:13.5px;font-weight:700;color:var(--white)}
.main-nav li.active{color:var(--lime)}
.search{left:841px;top:124px;width:232px;height:19px;background:var(--white);border:1px solid #063049;font-family:"Arimo",sans-serif;font-size:12px;color:#222;padding-left:6px;line-height:17px}
.search svg{position:absolute;right:5px;top:2px}

.video-frame{left:140px;top:163px;width:573px;height:332px;background:#f4f5f6;border:2px solid #d3d6d8;border-radius:10px;box-shadow:0 1px 3px rgba(0,0,0,.15)}
.video{left:160px;top:184px;width:532px;height:289px;background:var(--magenta);border:1px solid #7a2060}
.video-label{left:258px;top:280px;display:flex;align-items:center;gap:22px;color:var(--white)}
.video-icon{width:102px;height:80px;background:var(--magenta-light);border-radius:2px}
.video-title{font-size:86px;font-weight:800;line-height:68px;letter-spacing:1px}
.video-sub{font-size:17px;font-weight:800;letter-spacing:.5px;margin-top:-1px}
.dots{left:653px;top:480px;display:flex;gap:7px}
.dots i{width:8px;height:8px;border-radius:50%;background:#7f9fb5;display:block}

.pitch{left:738px;top:150px;width:311px;height:345px;background:linear-gradient(#0b3d5e,#0f5580);border-radius:0 0 8px 8px;color:var(--white)}
.pitch h2{position:absolute;left:17px;top:25px;font-size:20px;font-weight:400;letter-spacing:-.3px}
.pitch h2 b{font-weight:800}
.pitch h3{position:absolute;left:17px;font-size:15px;font-weight:400}
.pitch .builders{top:64px;color:var(--panel-light)}
.pitch .funders{top:198px;color:var(--lime)}
.pitch ul{position:absolute;left:63px;list-style:none;font-size:15px;line-height:19px}
.pitch li::before{content:"+";display:inline-block;width:12px;height:12px;border-radius:50%;border:1px solid #5b86a8;font-size:10px;line-height:10px;text-align:center;margin-right:8px;color:#8fb5d3;vertical-align:1px}
.pitch ul.for-builders{top:85px}
.pitch ul.for-funders{top:219px}
.pitch ul.for-funders li::before{border-color:var(--green);color:var(--green)}
.btn{position:absolute;width:170px;height:36px;border-radius:3px;text-align:center;line-height:34px;font-size:17px;font-weight:600;color:var(--white)}
.btn-project{left:71px;top:152px;background:linear-gradient(#3c76d8,#1d4aa0);border:1px solid #7ea8e9}
.btn-funding{left:67px;top:283px;background:linear-gradient(#6fd236,#2f9a18);border:1px solid #9be36d}

.featured{left:156px;top:505px;font-size:13px;color:var(--muted)}
.press{left:160px;top:524px;width:880px;display:flex;justify-content:space-between;align-items:center;font-size:19px;font-weight:700;color:#9ca1a5;height:28px}

.section-bar{height:25px;line-height:25px;color:var(--white);font-size:14px;padding-left:17px}
.section-bar .more{position:absolute;right:10px;font-size:11px;font-weight:700}
.bar-apps{left:140px;width:573px;background:var(--navy)}
.bar-funders{left:738px;top:581px;width:312px;background:var(--green)}
.bar-funders em{font-style:normal;color:var(--navy-dark)}

.app{position:absolute;width:96px;text-align:center}
.app .icon{width:96px;height:92px;border-radius:12px;border:3px solid #555;box-shadow:0 2px 4px rgba(0,0,0,.4)}
.app span{display:block;margin-top:8px;font-size:11px;color:var(--navy-dark)}

.funder{position:absolute;width:78px;text-align:center}
.funder .photo{width:78px;height:78px;border:3px solid #2f4f6f;border-radius:8px;background:linear-gradient(#d8d8d8,#9a9a9a)}
.funder span{display:block;margin-top:4px;font-size:12px;font-weight:700;color:#333}
</style>
</head>
<body>

<header class="site-header abs">
  <div class="hero-art abs" role="img" aria-label="Illustration of a cheerful boy holding a phone beside a smartphone bursting with colourful app icons"></div>
  <div class="brand abs"><span class="brand-mark"></span><span class="brand-name">PledgeBloom</span></div>
  <nav class="utility abs"><span>Blog</span><span class="sep">|</span><span>Get AAA Certified</span><span class="sep">|</span><span>About us</span><span class="sep">|</span><span>Login in</span></nav>
  <div class="lang abs">SELECT LANGAUGE</div>
  <div class="social abs" aria-label="Social links"><i></i><i></i><i></i><i></i><i></i></div>
</header>

<nav class="main-nav abs">
  <ul>
    <li class="active">HOME</li><li>FUND&nbsp; APPS</li><li>SUBMIT YOUR APP</li><li>FIND A DEVELOPER</li><li>HOW IT WORKS</li><li>REGISTER</li>
  </ul>
</nav>
<div class="search abs">Search
  <svg width="14" height="14" viewBox="0 0 14 14"><circle cx="5.5" cy="5.5" r="4.2" fill="none" stroke="#000" stroke-width="2"/><line x1="8.6" y1="8.6" x2="13" y2="13" stroke="#000" stroke-width="2.4"/></svg>
</div>

<div class="video-frame abs"></div>
<div class="video abs"></div>
<div class="video-label abs">
  <div class="video-icon" role="img" aria-label="Cassette tape icon"></div>
  <div><div class="video-title">PLAY</div><div class="video-sub">INTRODUCTORY VIDEO</div></div>
</div>
<div class="dots abs"><i></i><i></i><i></i></div>

<aside class="pitch abs">
  <h2>SUPPORT <b>NEW MOBILE APPS</b></h2>
  <h3 class="builders">APP BUILDERS:</h3>
  <ul class="for-builders"><li>Fund your development</li><li>Build up customers</li><li>Keep 100% ownership</li></ul>
  <a class="btn btn-project">Start project</a>
  <h3 class="funders">FUNDERS:</h3>
  <ul class="for-funders"><li>Up to 120% in return</li><li>Fund per milestone</li><li>Get appstore sales updates</li></ul>
  <a class="btn btn-funding">Start funding</a>
</aside>

<div class="featured abs">Featured on :</div>
<div class="press abs"><span>The Harbor Ledger</span><span>ByteDesk</span><span>infowire</span><span style="font-weight:400">StartIndex</span><span>FoundryPulse</span></div>

<div class="section-bar bar-apps abs" style="top:581px">Most funded apps:<span class="more">see all&gt;&gt;</span></div>
<div class="app" style="left:146px;top:620px"><div class="icon" role="img" aria-label="Cliffdash game icon with jungle scenery" style="background:linear-gradient(#3f7a2e,#8a5a22)"></div><span>GridOtter</span></div>
<div class="app" style="left:262px;top:620px"><div class="icon" role="img" aria-label="App icon with cartoon panda on red" style="background:linear-gradient(#e02b2b,#9e1414)"></div><span>GridOtter</span></div>
<div class="app" style="left:378px;top:620px"><div class="icon" role="img" aria-label="App icon with orange letter and signal on dark grey" style="background:linear-gradient(#6a6a6a,#3a3a3a)"></div><span>GridOtter</span></div>
<div class="app" style="left:494px;top:620px"><div class="icon" role="img" aria-label="App icon with chalkboard sketch" style="background:linear-gradient(#2b2b2b 70%,#b07a3a 70%)"></div><span>GridOtter</span></div>
<div class="app" style="left:610px;top:620px"><div class="icon" role="img" aria-label="App icon with cartoon panda on red" style="background:linear-gradient(#e02b2b,#9e1414)"></div><span>GridOtter</span></div>

<div class="section-bar bar-apps abs" style="top:757px">Most funded apps:<span class="more">see all&gt;&gt;</span></div>
<div class="app" style="left:146px;top:795px"><div class="icon" style="background:#666"></div></div>
<div class="app" style="left:262px;top:795px"><div class="icon" style="background:#666"></div></div>
<div class="app" style="left:378px;top:795px"><div class="icon" style="background:#666"></div></div>
<div class="app" style="left:494px;top:795px"><div class="icon" style="background:#666"></div></div>
<div class="app" style="left:610px;top:795px"><div class="icon" style="background:#666"></div></div>

<div class="section-bar bar-funders abs">Most Active <em>Funders:</em></div>
<div class="funder" style="left:755px;top:626px"><div class="photo" role="img" aria-label="Funder silhouette placeholder" style="background:linear-gradient(#f0f0f0,#bdbdbd)"></div><span>Tov</span></div>
<div class="funder" style="left:856px;top:626px"><div class="photo" role="img" aria-label="Funder portrait photo"></div><span>Henrik D...</span></div>
<div class="funder" style="left:958px;top:626px"><div class="photo" role="img" aria-label="Funder portrait photo" style="background:linear-gradient(#cfcfcf,#6f6f6f)"></div><span>Marcel ...</span></div>
<div class="funder" style="left:755px;top:728px"><div class="photo" role="img" aria-label="Funder outdoor photo" style="background:linear-gradient(#bcbcbc,#5a5a5a)"></div></div>
<div class="funder" style="left:856px;top:728px"><div class="photo" role="img" aria-label="Default funder avatar" style="background:linear-gradient(#f5f5f5,#c7c7c7)"></div></div>
<div class="funder" style="left:958px;top:728px"><div class="photo" role="img" aria-label="Funder gear avatar" style="background:linear-gradient(#e8e8e8,#444)"></div></div>

</body>
</html>
```